Business Card Design

We Need a business card design for my company based in Tv Radio and music Productions and hunt Talent.

Industry/Entity Type

Business

Contact Information for Business Card

BrentaVue Production's, Teodor Vignoles,Cell Phone 318 4957310
Musician, Productor, Hunt Talent. Miami Fla. www.brentavue.net Mail. teodorvignoles@mailvana.com

```html
<!DOCTYPE html>
<html lang="en">
<head>
<meta charset="utf-8">
<title>BrentaVue Production's – Business Card</title>
<link rel="stylesheet" href="https://fonts.googleapis.com/css2?family=Cinzel:wght@700&family=Cormorant+Garamond:ital,wght@1,500&display=swap">
<style>
  :root {
    --paper: #ffffff;
    --ink: #111111;
    --rule-red: #b3362c;
    --halftone-grey: #c9cacc;
    --halftone-fade: #eeeff0;
  }
  html, body {
    margin: 0;
    padding: 0;
    overflow: hidden;
    background: var(--paper);
  }
  .card {
    position: relative;
    width: 1200px;
    height: 753px;
    background: var(--paper);
    overflow: hidden;
  }
  .texture-area {
    position: absolute;
    left: 405px;
    top: 105px;
    width: 390px;
    height: 545px;
    border-radius: 40px;
    background: radial-gradient(ellipse at 50% 40%, var(--halftone-grey) 0%, var(--halftone-fade) 75%, var(--paper) 100%);
  }
  .rule {
    position: absolute;
    height: 2px;
    background: var(--rule-red);
  }
  .rule--top { left: 357px; top: 296px; width: 490px; }
  .rule--bottom { left: 434px; top: 435px; width: 335px; }
  .headline {
    position: absolute;
    left: 250px;
    top: 327px;
    width: 704px;
    margin: 0;
    text-align: center;
    font-family: "Cinzel", serif;
    font-weight: 700;
    font-size: 30px;
    line-height: 40px;
    letter-spacing: 0.6px;
    text-transform: uppercase;
    color: var(--ink);
  }
  .headline span { display: block; }
  .contact {
    position: absolute;
    left: 250px;
    top: 479px;
    width: 704px;
    margin: 0;
    padding: 0;
    list-style: none;
    text-align: center;
    font-family: "Cormorant Garamond", serif;
    font-style: italic;
    font-weight: 500;
    font-size: 28px;
    line-height: 40.5px;
    letter-spacing: 0.3px;
    font-variant-numeric: lining-nums;
    color: var(--ink);
  }
  .brand-mark {
    position: absolute;
    left: 888px;
    top: 170px;
    width: 200px;
    display: flex;
    align-items: center;
    gap: 8px;
    font-family: "Cinzel", serif;
    font-weight: 700;
    font-size: 19px;
    color: var(--ink);
  }
  .brand-mark__dot {
    width: 16px;
    height: 16px;
    border-radius: 50%;
    background: var(--rule-red);
    flex: none;
  }
</style>
</head>
<body>
  <main class="card">
    <div class="texture-area" role="img" aria-label="Soft grey halftone dot texture behind the name and contact details"></div>

    <div class="rule rule--top"></div>
    <h1 class="headline">
      <span>BrentaVue Production's</span>
      <span>Teodor Vignoles</span>
    </h1>
    <div class="rule rule--bottom"></div>

    <ul class="contact">
      <li>Cell Phone 318 4957310</li>
      <li>Musician, Productor, Hunt Talent. Miami Fla.</li>
      <li>www.brentavue.net</li>
      <li>teodorvignoles@mailvana.com</li>
    </ul>

    <div class="brand-mark">
      <span class="brand-mark__dot"></span>
      <span class="brand-mark__name">BrentaVue Show</span>
    </div>
  </main>
</body>
</html>
```